Goat's Milk Soap

International product development company seeking designs for the following soap label:

Hand crafted in Mt Berryman QLD Australia, Lockyer Valley
Second Generation Goat Farmers
Soap is hand made in appearance but gives an instant soothing feel when used
High in Vegetable oils and pure fresh goats milk (no powders used)
Give the emotional feel of Quality and Hand crafted
Label must stimulate an emotional response visually
Label must deliver to the customer anticipation for use.
Would anticipate that the label will be produced on a matte finish brown paper label or similar.

Logo should be no larger than 50mm x 50mm
Label should measure around 120mm x 70mm

```html
<!DOCTYPE html>
<html lang="en">
<head>
<meta charset="utf-8">
<title>Goat's Milk Soap – Label Options</title>
<link rel="stylesheet" href="https://fonts.googleapis.com/css2?family=Della+Respira&display=swap">
<style>
  :root {
    --backdrop: #9e824f;
    --taupe: #857870;
    --cream: #ffffff;
  }
  * { margin: 0; padding: 0; box-sizing: border-box; }
  html, body {
    width: 1200px;
    height: 1200px;
    overflow: hidden;
    background: var(--backdrop);
  }
  .canvas {
    position: relative;
    width: 1200px;
    height: 1200px;
  }
  .label {
    position: absolute;
    left: 175px;
    width: 850px;
    height: 496px;
    border: 10px solid;
    font-family: "Della Respira", serif;
    text-align: center;
  }
  .label--dark {
    top: 55px;
    background: var(--taupe);
    border-color: var(--cream);
    color: var(--cream);
  }
  .label--light {
    top: 592px;
    background: var(--cream);
    border-color: var(--taupe);
    color: var(--taupe);
  }
  .brand {
    position: absolute;
    top: 130px;
    left: 0;
    right: 0;
    display: flex;
    justify-content: center;
    align-items: center;
    gap: 18px;
    font-size: 50px;
    line-height: 1;
  }
  .brand__dot {
    width: 30px;
    height: 30px;
    border-radius: 50%;
    background: currentColor;
  }
  .product-name {
    position: absolute;
    top: 295px;
    left: 0;
    right: 0;
    font-size: 72px;
    font-weight: 400;
    line-height: 1;
  }
  .tagline {
    position: absolute;
    top: 384px;
    left: 0;
    right: 0;
    font-size: 23px;
    line-height: 31px;
  }
</style>
</head>
<body>
  <main class="canvas">
    <section class="label label--dark">
      <div class="brand"><span class="brand__dot"></span><span>Hollow Creek</span></div>
      <h1 class="product-name">Goat’s Milk Soap</h1>
      <p class="tagline">Made from fresh Australia Goat’s Milk<br>100 grams</p>
    </section>

    <section class="label label--light">
      <div class="brand"><span class="brand__dot"></span><span>Hollow Creek</span></div>
      <h1 class="product-name">Goat’s Milk Soap</h1>
      <p class="tagline">Made from fresh Australia Goat’s Milk<br>100 grams</p>
    </section>
  </main>
</body>
</html>
```